The Web Promotion Playbook for Yard & Patio Construction Crews

We need a book cover design that is for a book targeting landscape and outdoor living contractors that helps them grow their business using online marketing.

We run a business focused on this industry so you can see what we do: https://yardcrewgrowthworks.com/

The title is: The Web Promotion Playbook for Yard & Patio Construction Crews

The author is: Trent Varnholm
Some drafts have been done however they're still looking basic and somewhat amateur, we're looking for something that will stand out.

Target Market(s)

Landscape, Hardscape and Outdoor Living Contractors and Business Owners

Industry/Entity Type

Online Marketing

Font styles to use
Serif
Sans Serif

Requirements
Must have
• The part of the title that should stand out the most is the text "Web Promotion Playbook".
Should not have
• The color red

```html
<!DOCTYPE html>
<html lang="en">
<head>
<meta charset="utf-8">
<title>The Web Promotion Playbook for Yard &amp; Patio Construction Crews</title>
<link rel="stylesheet" href="https://fonts.googleapis.com/css2?family=Oswald:wght@400;600&display=swap">
<style>
  :root {
    --page-bg: #dde3e7;
    --cover-dark: #010f06;
    --leaf-deep: #03200c;
    --leaf-mid: #0f4a22;
    --leaf-light: #1f6e35;
    --frame-line: #3fbf4a;
    --title-white: #ffffff;
    --accent-green: #1fd61f;
  }
  * { margin: 0; padding: 0; box-sizing: border-box; }
  html, body {
    width: 1200px;
    height: 848px;
    overflow: hidden;
    background: var(--page-bg);
  }
  .book-cover {
    position: absolute;
    left: 320px;
    top: 29px;
    width: 560px;
    height: 790px;
    background: var(--cover-dark);
    overflow: hidden;
  }
  .foliage-photo {
    position: absolute;
    left: 0;
    top: 0;
    width: 100%;
    height: 450px;
    background:
      radial-gradient(ellipse at 30% 30%, var(--leaf-light) 0%, transparent 55%),
      radial-gradient(ellipse at 75% 55%, var(--leaf-mid) 0%, transparent 60%),
      linear-gradient(180deg, var(--leaf-mid) 0%, var(--leaf-deep) 80%, #021509 100%);
  }
  .frame-lines {
    position: absolute;
    left: 0;
    top: 0;
    width: 560px;
    height: 790px;
  }
  .title-block {
    position: absolute;
    left: 90px;
    right: 90px;
    top: 352px;
    text-align: center;
    font-family: "Oswald", "Arial Narrow", sans-serif;
    text-transform: uppercase;
    font-weight: 400;
  }
  .title-lead {
    display: block;
    color: var(--title-white);
    font-size: 30px;
    line-height: 1.1;
    letter-spacing: 1px;
  }
  .title-main {
    display: block;
    color: var(--title-white);
    font-weight: 600;
    font-size: 50px;
    line-height: 1.05;
    letter-spacing: 0.5px;
  }
  .title-sub {
    display: block;
    margin-top: 10px;
    color: var(--accent-green);
    font-weight: 400;
    font-size: 28px;
    line-height: 1.15;
    letter-spacing: 0.5px;
  }
  .author-name {
    position: absolute;
    left: 200px;
    width: 160px;
    top: 678px;
    text-align: center;
    font-family: "Oswald", "Arial Narrow", sans-serif;
    text-transform: uppercase;
    color: var(--title-white);
    font-size: 32px;
    line-height: 1.1;
  }
</style>
</head>
<body>
  <main class="book-cover">
    <div class="foliage-photo" role="img" aria-label="Close-up photograph of dense dark green leaves"></div>
    <svg class="frame-lines" viewBox="0 0 560 790" aria-hidden="true">
      <g fill="none" stroke="var(--frame-line)" stroke-width="4">
        <polyline points="70,340 70,195 495,195 495,340"/>
        <polyline points="70,585 70,715 200,715"/>
        <polyline points="360,715 495,715 495,585"/>
      </g>
    </svg>
    <h1 class="title-block">
      <span class="title-lead">The</span>
      <span class="title-main">Web Promotion<br>Playbook</span>
      <span class="title-sub">For Yard &amp; Patio<br>Construction Crews</span>
    </h1>
    <p class="author-name">Trent<br>Varnholm</p>
  </main>
</body>
</html>
```